SUMMIT FACADE SERVICES / SFS SUSPENSION SPECIALIST

I would like something like this but with all of our info and logo. All the verbiage is good maybe redo some of the wording...

```html
<!DOCTYPE html>
<html lang="en">
<head>
<meta charset="utf-8">
<title>Summit Facade Services – Exterior Building Care Specialists</title>
<link rel="stylesheet" href="https://fonts.googleapis.com/css2?family=Poppins:ital,wght@0,400;0,500;0,600;0,800;1,700;1,800&display=swap">
<style>
  :root {
    --sky: #4a7ce0;
    --sky-deep: #2f5fd6;
    --band-red: #d10a0a;
    --band-dark: #0b2ea8;
    --white: #ffffff;
    --badge-yellow: #ffc400;
    --ink: #111111;
  }
  * { margin: 0; padding: 0; box-sizing: border-box; }
  html, body { width: 927px; height: 1200px; overflow: hidden; }
  body { font-family: "Poppins", sans-serif; color: var(--white); }

  .flyer { position: relative; width: 927px; height: 1200px; overflow: hidden; }
  .backdrop {
    position: absolute; inset: 0;
    background: linear-gradient(160deg, #3f6fdc 0%, #5a8bea 45%, #4a7ce0 70%, #3d6cd8 100%);
  }

  .site-url {
    position: absolute; top: 40px; right: 63px;
    font-size: 19px; font-weight: 700; font-style: italic;
  }

  .title-band {
    position: absolute; top: 75px; left: 0; width: 927px; height: 83px;
    border-top: 4px solid var(--white); border-bottom: 4px solid var(--white);
    background: var(--band-red);
  }
  .title-band .half {
    position: absolute; top: 0; height: 75px; line-height: 75px;
    font-size: 29px; font-weight: 800; font-style: italic;
  }
  .title-band .left { left: 63px; }
  .title-band .right { left: 576px; }
  .brand-box {
    position: absolute; top: -4px; left: 365px; width: 196px; height: 83px;
    border-left: 4px solid var(--white); border-right: 4px solid var(--white);
    display: flex; align-items: center; justify-content: center;
  }
  .brand-name { font-size: 38px; font-weight: 800; letter-spacing: 1px; color: var(--white); }

  .photo {
    position: absolute; top: 188px; height: 129px;
    border: 5px solid var(--white); border-radius: 4px;
  }
  .photo-1 { left: 25px; width: 211px; background: linear-gradient(180deg, #b9c4cf, #8d8f8c 60%, #6d7a6a); }
  .photo-2 { left: 248px; width: 210px; background: linear-gradient(180deg, #cdd3d9, #9aa3aa 60%, #6f6a60); }
  .photo-3 { left: 470px; width: 210px; background: linear-gradient(180deg, #7fb4e6, #a6a9a4 55%, #7a6e5a); }
  .photo-4 { left: 692px; width: 209px; background: linear-gradient(180deg, #2a86e4, #5aa8ef 60%, #c9ccd0); }

  .intro {
    position: absolute; left: 108px; width: 720px;
    font-size: 16.4px; font-weight: 500; line-height: 24.5px; text-align: justify;
  }
  .intro-about { top: 335px; }
  .intro-mission { top: 477px; }

  .services-heading {
    position: absolute; top: 587px; left: 105px; width: 740px;
    font-size: 21.5px; font-weight: 700; font-style: italic; line-height: 25px;
  }
  .services-list {
    position: absolute; top: 657px; left: 140px; list-style: none;
    font-size: 19px; font-weight: 400; line-height: 27.4px;
  }
  .services-list li::before { content: "•"; margin-right: 10px; }

  .response-badge { position: absolute; top: 700px; left: 668px; width: 182px; height: 182px; }
  .response-badge .label {
    position: absolute; inset: 0; display: flex; flex-direction: column;
    align-items: center; justify-content: center; color: var(--ink);
    font-weight: 800; font-style: italic; text-align: center;
  }
  .response-badge .big { font-size: 43px; line-height: 46px; font-style: normal; }
  .response-badge .small { font-size: 18px; line-height: 24px; }

  .contact-band {
    position: absolute; top: 963px; left: 0; width: 927px; height: 192px;
    background: var(--band-dark); opacity: 0.95;
  }
  .contact-invite {
    position: absolute; top: 979px; left: 0; width: 880px; text-align: center;
    font-size: 15.5px; font-weight: 700; font-style: italic; line-height: 24px;
  }
  .contact-phone {
    position: absolute; top: 1035px; left: 286px; width: 358px; height: 62px;
    background: var(--band-red); border: 3px solid var(--white); border-radius: 31px;
    text-align: center; line-height: 56px;
    font-size: 37px; font-weight: 800; font-style: italic;
  }
  .contact-email {
    position: absolute; top: 1102px; left: 0; width: 927px; text-align: center;
    font-size: 26px; font-weight: 700; font-style: italic;
  }
</style>
</head>
<body>
<main class="flyer">
  <div class="backdrop" role="img" aria-label="Blue-tinted rooftop with davit arms behind the content"></div>

  <div class="site-url">www.sumfac-demo.net</div>

  <header class="title-band">
    <span class="half left">Exterior Building</span>
    <div class="brand-box"><span class="brand-name">SFS INC.</span></div>
    <span class="half right">Care Specialists</span>
  </header>

  <div class="photo photo-1" role="img" aria-label="Crew in safety vests on a rooftop edge"></div>
  <div class="photo photo-2" role="img" aria-label="Suspended work platform hanging over a city"></div>
  <div class="photo photo-3" role="img" aria-label="Worker welding a rooftop anchor"></div>
  <div class="photo photo-4" role="img" aria-label="Roof davit arms against a blue sky"></div>

  <p class="intro intro-about">SFS, with 42 years of expertise in the suspended scaffold and access industry, specializes in exterior building maintenance systems. This includes working at heights and ensuring compliance with OSHA safety standards. Our focus is on adapting existing building maintenance systems, particularly window cleaning systems, to align with OSHA regulations.</p>

  <p class="intro intro-mission">Our mission is centered on enabling you to furnish the essential exterior building maintenance equipment, enhancing worker safety, safeguarding the public, averting accidents, sidestepping OSHA penalties, and preserving your assets during elevated work on your building.</p>

  <h2 class="services-heading">We offer a range of services to ensure that your company and equipment remain compliant and well-maintained:</h2>

  <ul class="services-list">
    <li>Engineering &amp; Design</li>
    <li>Fall Protection</li>
    <li>Powered Platforms &amp; Suspension Equipment</li>
    <li>Installation</li>
    <li>Testing &amp; Certification</li>
    <li>Retrofitting</li>
    <li>Annual Inspections</li>
    <li>Pre-use Inspections</li>
    <li>OPOS Document/Work Plan</li>
    <li>Training</li>
  </ul>

  <div class="response-badge">
    <svg width="182" height="182" viewBox="0 0 182 182" aria-hidden="true">
      <polygon points="53,1 129,1 181,53 181,129 129,181 53,181 1,129 1,53" fill="var(--badge-yellow)"/>
      <polygon points="57,11 125,11 171,57 171,125 125,171 57,171 11,125 11,57" fill="none" stroke="var(--ink)" stroke-width="4"/>
    </svg>
    <div class="label">
      <span class="big">24HR</span>
      <span class="small">RESPONSE<br>POLICY</span>
    </div>
  </div>

  <div class="contact-band"></div>
  <p class="contact-invite">Let's collaborate to make certain that your building is a secure working environment,<br>and access equipment is properly looked after.</p>
  <div class="contact-phone">555-014-2290</div>
  <div class="contact-email">sfs@sumfac-demo.net</div>
</main>
</body>
</html>
```